Harbor Kestrel
Your Trusted Advisors
Professional
Rosalind Okafor
Partner
418 Tamarack Lane
Cedar Hollow, VT 05388
rosalind.okafor@harborkestrel.co
www.harborkestrel.co

```html
<!DOCTYPE html>
<html lang="en">
<head>
<meta charset="utf-8">
<title>Harbor Kestrel — Stationery</title>
<link rel="stylesheet" href="https://fonts.googleapis.com/css2?family=Montserrat:wght@700&family=Open+Sans:wght@400;600&display=swap">
<style>
  :root {
    --red: #b3141c;
    --red-dark: #7d0a10;
    --red-light: #d9363c;
    --ink: #333333;
    --grey: #6d6d6d;
    --paper: #ffffff;
    --backdrop: #e9e6e1;
    --black-line: #2a2a2a;
    --ghost: rgba(179,20,28,.07);
  }
  * { margin: 0; padding: 0; box-sizing: border-box; }
  html, body { width: 1200px; height: 782px; overflow: hidden; }
  body { background: var(--backdrop); font-family: "Open Sans", Arial, sans-serif; color: var(--ink); position: relative; }

  .brand-name { font-family: "Montserrat", Arial, sans-serif; font-weight: 700; color: var(--red); letter-spacing: 0.5px; white-space: nowrap; }
  .brand-mark { display: inline-block; flex: none; border-radius: 50%; background: var(--red); }

  .contact { font-size: 8px; line-height: 1.5; color: var(--grey); white-space: nowrap; }
  .contact b { color: var(--ink); font-weight: 600; }
  .band { position: absolute; left: 0; right: 0; background: linear-gradient(to bottom, var(--red-light), var(--red-dark)); border-top: 3px solid var(--black-line); }

  /* Letterhead */
  .letterhead { position: absolute; left: 233px; top: 43px; width: 559px; height: 682px; background: var(--paper); box-shadow: 0 2px 8px rgba(0,0,0,.12); }
  .letterhead .brand { position: absolute; left: 62px; top: 34px; display: flex; align-items: center; gap: 8px; }
  .letterhead .brand-name { font-size: 20px; }
  .letterhead .brand-mark { width: 20px; height: 20px; }
  .letterhead .divider { position: absolute; left: 342px; top: 34px; width: 1px; height: 58px; background: #bbb; }
  .letterhead .contact { position: absolute; left: 350px; top: 32px; }
  .letterhead .band { bottom: 0; height: 16px; }

  /* Envelope */
  .envelope { position: absolute; left: 494px; top: 245px; width: 572px; height: 302px; background: var(--paper); box-shadow: 0 2px 8px rgba(0,0,0,.15); }
  .envelope .flap { position: absolute; left: 0; top: 0; }
  .envelope .flap-name { position: absolute; left: 0; right: 0; top: 20px; text-align: center; }
  .envelope .flap-name .brand-name { color: var(--paper); font-size: 15px; }
  .envelope .ghost { position: absolute; right: 30px; top: 200px; }
  .envelope .ghost .brand-name { font-size: 17px; color: var(--ghost); }
  .envelope .brand { position: absolute; left: 44px; top: 132px; display: flex; align-items: center; gap: 6px; }
  .envelope .brand-name { font-size: 15px; }
  .envelope .brand-mark { width: 13px; height: 13px; }
  .envelope .contact { position: absolute; left: 20px; top: 204px; font-size: 7.5px; }
  .envelope .band { bottom: 0; height: 18px; }

  /* Business cards */
  .card { position: absolute; left: 34px; width: 322px; border-radius: 16px; overflow: hidden; box-shadow: 0 2px 8px rgba(0,0,0,.15); }
  .card-front { top: 187px; height: 192px; background: var(--paper); }
  .card-front .brand { position: absolute; left: 24px; top: 28px; display: flex; align-items: center; gap: 6px; }
  .card-front .brand-name { font-size: 14px; }
  .card-front .brand-mark { width: 13px; height: 13px; }
  .card-front .person { position: absolute; left: 24px; top: 96px; }
  .card-front .person-name { font-size: 12px; color: var(--red); }
  .card-front .person-role { font-size: 7.5px; color: var(--grey); margin-top: 2px; }
  .card-front .divider { position: absolute; left: 128px; top: 96px; width: 1px; height: 56px; background: #bbb; }
  .card-front .contact { position: absolute; left: 134px; top: 94px; font-size: 7px; }
  .card-front .band { bottom: 0; height: 22px; }

  .card-back { top: 439px; height: 180px; background: radial-gradient(ellipse at 50% 40%, var(--red-light), var(--red) 55%, var(--red-dark)); }
  .card-back .brand { position: absolute; left: 0; right: 0; top: 70px; display: flex; justify-content: center; align-items: center; gap: 8px; }
  .card-back .brand-name { color: var(--paper); font-size: 18px; }
  .card-back .brand-mark { width: 15px; height: 15px; background: var(--paper); }
  .card-back .web { position: absolute; left: 0; right: 0; top: 140px; text-align: center; font-size: 8.5px; color: var(--paper); }
</style>
</head>
<body>

  <section class="letterhead" aria-label="Letterhead">
    <div class="brand"><span class="brand-mark"></span><span class="brand-name">HARBOR KESTREL</span></div>
    <div class="divider"></div>
    <div class="contact">
      418 Tamarack Lane<br>
      Cedar Hollow, VT 05388<br>
      <b>Cell :</b> 555 014 2210<br>
      <b>Email :</b> rosalind.okafor@harborkestrel.co<br>
      <b>Web :</b> www.harborkestrel.co
    </div>
    <div class="band"></div>
  </section>

  <section class="envelope" aria-label="Envelope">
    <svg class="flap" width="572" height="100" viewBox="0 0 572 100">
      <defs>
        <linearGradient id="flapFill" x1="0" y1="0" x2="0" y2="1">
          <stop offset="0" stop-color="#d9363c"/>
          <stop offset="1" stop-color="#7d0a10"/>
        </linearGradient>
      </defs>
      <path d="M0 0 H572 V40 Q560 34 530 42 L325 88 Q286 98 247 88 L42 42 Q12 34 0 40 Z" fill="url(#flapFill)"/>
    </svg>
    <div class="flap-name"><span class="brand-name">HARBOR KESTREL</span></div>
    <div class="ghost"><span class="brand-name">HARBOR KESTREL</span></div>
    <div class="brand"><span class="brand-mark"></span><span class="brand-name">HARBOR KESTREL</span></div>
    <div class="contact">
      418 Tamarack Lane<br>
      Cedar Hollow, VT 05388<br>
      <b>Cell :</b> 555 014 2210<br>
      <b>Email :</b> rosalind.okafor@harborkestrel.co<br>
      <b>Web :</b> www.harborkestrel.co
    </div>
    <div class="band"></div>
  </section>

  <section class="card card-front" aria-label="Business card front">
    <div class="brand"><span class="brand-mark"></span><span class="brand-name">HARBOR KESTREL</span></div>
    <div class="person">
      <div class="person-name">Rosalind Okafor</div>
      <div class="person-role">Partner</div>
    </div>
    <div class="divider"></div>
    <div class="contact">
      418 Tamarack Lane<br>
      Cedar Hollow, VT 05388<br>
      <b>Cell :</b> 555 014 2210<br>
      <b>Email :</b> rosalind.okafor@harborkestrel.co
    </div>
    <div class="band"></div>
  </section>

  <section class="card card-back" aria-label="Business card back">
    <div class="brand"><span class="brand-mark"></span><span class="brand-name">HARBOR KESTREL</span></div>
    <div class="web">www.harborkestrel.co</div>
  </section>

</body>
</html>
```